Tess Marlowe Communication business card

I am starting a small, country-based business that offers writing, communication and marketing services to a wide range of clients, inner city big business, to mining, through to agriculture.

The appeal of my business is that it's mobile and flexible. It's just me, with lots of hands-on experience on construction and infrastructure projects.

I can provide the following services:

• Communication planning and management
• Issues and media management
• Marketing and communication materials
• Project management and strategy
• Government liaison
• Incident management communication
• Stakeholder management

It would be great to be able to use the elements of the business card design on other stationery.

Industry/Entity Type

Communication

Requirements
Must have
• The following information:

Tess Marlowe
M: 0427 391 864
E: tess@tmcommsmail.com

PO Box 152
Durrandale Q 4472
Nice to have
• a rural element (windmill, workboots, wheat stalk)

```html
<!DOCTYPE html>
<html lang="en">
<head>
<meta charset="utf-8">
<title>Tess Marlowe Communication – Business Card</title>
<link href="https://fonts.googleapis.com/css2?family=Saira+Semi+Condensed:wght@400;500;600&display=swap" rel="stylesheet">
<style>
  :root {
    --page-bg: #ebe8df;
    --card-blue: #0b4a93;
    --mill-blue: #1465ad;
    --tag-grey: #8b8b8b;
    --sky-blue: #1a93dc;
    --ink-navy: #1c3f80;
    --divider-blue: #8fc9ee;
    --white: #ffffff;
  }
  * { box-sizing: border-box; margin: 0; padding: 0; }
  html, body {
    width: 1200px; height: 900px; overflow: hidden;
    background: var(--page-bg);
    font-family: "Saira Semi Condensed", "Arial Narrow", "Roboto Condensed", sans-serif;
  }
  .stage { position: relative; width: 1200px; height: 900px; }

  /* Front of card */
  .card-front {
    position: absolute; left: 73px; top: 57px;
    width: 654px; height: 423px;
    background: var(--card-blue);
    overflow: hidden;
  }
  .windmill-art {
    position: absolute; left: 312px; top: 0;
    width: 342px; height: 362px;
  }
  .brand {
    position: absolute; left: 38px; top: 228px;
    color: var(--white); font-weight: 500; line-height: 1;
    white-space: nowrap;
  }
  .brand-name { display: block; font-size: 48px; letter-spacing: 0.5px; text-transform: lowercase; }
  .brand-sub {
    display: block; font-size: 17px; letter-spacing: 1px;
    text-transform: lowercase; margin: 2px 0 0 140px;
  }
  .tagline-band {
    position: absolute; left: 285px; top: 360px;
    width: 369px; height: 35px;
  }
  .tagline {
    position: absolute; left: 285px; top: 360px;
    width: 369px; height: 35px;
    padding-right: 22px;
    display: flex; align-items: center; justify-content: flex-end;
    color: var(--white); font-size: 18px; font-weight: 500; letter-spacing: 0.3px;
    white-space: nowrap;
  }

  /* Back of card */
  .card-back {
    position: absolute; left: 556px; top: 467px;
    width: 601px; height: 389px;
    background: var(--white);
    overflow: hidden;
  }
  .contact {
    position: absolute; left: 58px; top: 64px;
    color: var(--ink-navy); font-size: 20px; font-weight: 500; line-height: 26.5px;
    font-style: normal; white-space: nowrap;
  }
  .contact .label { color: var(--sky-blue); }
  .contact .postal { margin-top: 26px; }
  .services-band {
    position: absolute; left: 23px; top: 249px;
    width: 554px; height: 121px;
  }
  .services {
    position: absolute; left: 23px; top: 256px;
    width: 554px; padding-right: 14px;
    list-style: none; text-align: right;
    color: var(--white); font-size: 18px; font-weight: 500; line-height: 27px;
    letter-spacing: -0.1px;
  }
  .services li { white-space: nowrap; }
  .services .sep { color: var(--divider-blue); padding: 0 3px; }
</style>
</head>
<body>
<main class="stage">

  <section class="card-front" aria-label="Card front">
    <svg class="windmill-art" viewBox="0 0 342 362" role="img" aria-label="Rural windmill silhouette illustration">
      <defs>
        <linearGradient id="millFade" x1="0" y1="0" x2="0" y2="1">
          <stop offset="0" stop-color="#1465ad" stop-opacity="0.15"/>
          <stop offset="1" stop-color="#1465ad" stop-opacity="0.85"/>
        </linearGradient>
      </defs>
      <rect width="342" height="362" fill="url(#millFade)"/>
    </svg>

    <div class="brand">
      <span class="brand-name">tess marlowe</span>
      <span class="brand-sub">communication</span>
    </div>

    <svg class="tagline-band" viewBox="0 0 369 35" aria-hidden="true">
      <polygon points="0,0 369,0 369,35 12,35 0,20" fill="var(--tag-grey)"/>
    </svg>
    <p class="tagline">“...mobile, flexible, and experienced!”</p>
  </section>

  <section class="card-back" aria-label="Card back">
    <address class="contact">
      <div>Tess Marlowe</div>
      <div><span class="label">M:</span> 0427 391 864</div>
      <div><span class="label">E:</span> tess@tmcommsmail.com</div>
      <div class="postal">PO Box 152</div>
      <div>Durrandale Q 4472</div>
    </address>

    <svg class="services-band" viewBox="0 0 554 121" aria-hidden="true">
      <polygon points="0,0 554,0 554,121 40,121 0,95" fill="var(--sky-blue)"/>
    </svg>
    <ul class="services">
      <li>Issues and media management<span class="sep">|</span>Project management and strategy</li>
      <li>Government liaison<span class="sep">|</span>Incident management communication</li>
      <li>Communication planning and management</li>
      <li>Stakeholder management<span class="sep">|</span>Marketing and communication</li>
    </ul>
  </section>

</main>
</body>
</html>
```